Organic Soap Packaging

We need a package design for a new company called Willow Naturals. Our primary product is organic soap. Our business model is based on the social entrepreneurial concept of by one give one like Brend shoes. We are giving soap to help prevent the spread of disease; 1.4 million deaths a year can be prevented by hand washing.

The design is for a recycled cardboard box/package. We want to demonstrate the high end, luxury feel of the product with undertones of organic/earth friendly/social conscious.

The soap is small batch, spa like, essential oil scented all natural luxury.
Updates

I am very excited about this startup business and I believe we will have great success! I am passionate about organic personal care and helping others in need. If you share my passion, please bring your work to the table!

Target Market(s)

My target market is people who are educated through college. Health conscious, socially conscious, Generation X. Basically shoppers of Green Basket and Haverline.

Industry/Entity Type

Business

Requirements
Must have
• Suitable for Face, Hair, and Skin
Scented with Organic Essential Oils

```html
<!DOCTYPE html>
<html lang="en">
<head>
<meta charset="utf-8">
<title>Willow Naturals – Soap Packaging</title>
<link href="https://fonts.googleapis.com/css2?family=Marcellus&family=Caveat:wght@500&display=swap" rel="stylesheet">
<style>
  :root {
    --olive: #5f7236;
    --olive-dark: #4e5e2b;
    --leaf: #a5b86a;
    --slate-blue: #3b5a7a;
    --lilac: #c3a1d0;
    --plum: #6e5f68;
    --kraft: #c4a36c;
    --kraft-light: #dcc596;
    --cream: #e6d4ae;
    --blush: #f8e3d5;
    --white: #ffffff;
  }
  * { box-sizing: border-box; margin: 0; padding: 0; }
  html, body { width: 904px; height: 1200px; overflow: hidden; background: var(--white); }
  .sheet { position: relative; width: 904px; height: 1200px; }

  .brand { font-family: "Marcellus", serif; white-space: nowrap; display: flex; align-items: center; gap: 8px; }
  .brand-mark { width: 14px; height: 14px; display: inline-block; }
  .script { font-family: "Caveat", cursive; font-weight: 500; white-space: nowrap; }

  /* palette */
  .palette { position: absolute; top: 0; left: 565px; display: flex; gap: 12px; }
  .swatch { width: 58px; height: 39px; }

  /* dieline */
  .panel { position: absolute; }
  .lid { left: 62px; top: 16px; width: 305px; height: 110px; background: linear-gradient(#cfae76, var(--kraft)); }
  .flap-left { left: 12px; top: 126px; width: 50px; height: 117px; background: var(--kraft); clip-path: polygon(0 12%, 100% 0, 100% 100%, 0 88%); }
  .flap-right { left: 367px; top: 126px; width: 63px; height: 117px; background: var(--kraft); clip-path: polygon(0 0, 100% 12%, 100% 88%, 0 100%); }
  .back { left: 62px; top: 126px; width: 305px; height: 117px; background: var(--kraft); }
  .back-band { position: absolute; left: 0; top: 44px; width: 100%; height: 64px; background: var(--olive); display: flex; align-items: center; justify-content: center; }
  .back-oval { width: 150px; height: 40px; border-radius: 50%; background: var(--cream); display: flex; align-items: center; justify-content: center; transform: rotate(180deg); color: var(--olive); font-size: 15px; }
  .front { left: 62px; top: 243px; width: 305px; height: 172px; background: linear-gradient(160deg, #eadbb9, var(--kraft-light) 70%, var(--kraft)); }
  .front .brand { position: absolute; left: 45px; top: 32px; font-size: 24px; color: var(--olive); }
  .front .script { position: absolute; left: 142px; top: 66px; font-size: 14px; color: var(--olive); }
  .bottom { left: 12px; top: 415px; width: 418px; height: 113px; background: var(--kraft); clip-path: polygon(0 10%, 12% 0, 88% 0, 100% 10%, 100% 90%, 88% 100%, 12% 100%, 0 90%); }
  .bottom-band { position: absolute; left: 50px; top: 0; width: 305px; height: 56px; background: var(--olive); color: var(--white); display: flex; flex-direction: column; align-items: center; justify-content: center; }
  .bottom-band .brand { font-size: 22px; }
  .bottom-band .script { font-size: 14px; color: var(--leaf); }

  .art { position: absolute; }

  /* labels */
  .label { position: absolute; top: 578px; width: 346px; height: 297px; background: var(--cream); }
  .label-green { left: 34px; }
  .label-plum { left: 512px; }
  .label-top { height: 32px; }
  .label-frame { position: absolute; left: 26px; top: 56px; right: 26px; bottom: 70px; border: 2px solid; display: flex; flex-direction: column; align-items: center; justify-content: center; gap: 10px; }
  .label-frame .brand { font-size: 24px; }
  .label-frame .script { font-size: 17px; }
  .label-foot { position: absolute; left: 0; bottom: 0; width: 100%; height: 42px; display: flex; align-items: center; padding-left: 42px; }
  .label-foot .script { font-size: 15px; }
  .label-green .label-top, .label-green .label-foot { background: var(--olive); }
  .label-green .label-frame { border-color: var(--olive); color: var(--olive); }
  .label-green .label-foot .script { color: var(--leaf); }
  .label-plum .label-top, .label-plum .label-foot { background: var(--plum); }
  .label-plum .label-frame { border-color: var(--plum); color: var(--plum); }
  .label-plum .label-foot .script { color: var(--lilac); }

  /* sleeve */
  .sleeve { position: absolute; left: 231px; top: 895px; width: 444px; height: 260px; background: var(--blush); }
  .sleeve-top { position: absolute; top: 8px; width: 100%; text-align: center; font-size: 15px; color: var(--leaf); }
  .sleeve-band { position: absolute; left: 0; top: 76px; width: 100%; height: 78px; background: var(--olive); display: flex; align-items: center; justify-content: center; color: var(--white); }
  .sleeve-band .brand { font-size: 36px; gap: 14px; }
  .sleeve-band .brand-mark { width: 22px; height: 22px; background: var(--white); }
  .sleeve-foot { position: absolute; top: 196px; width: 100%; text-align: center; font-size: 17px; color: var(--olive); }
</style>
</head>
<body>
<main class="sheet">

  <div class="palette">
    <span class="swatch" style="background: var(--leaf)"></span>
    <span class="swatch" style="background: var(--olive)"></span>
    <span class="swatch" style="background: var(--slate-blue)"></span>
    <span class="swatch" style="background: var(--lilac)"></span>
    <span class="swatch" style="background: var(--plum)"></span>
  </div>

  <section class="dieline">
    <div class="panel lid">
      <div class="art" role="img" aria-label="Light green vine flourish ornament" style="left:70px;top:8px;width:170px;height:36px;border-radius:18px;background:radial-gradient(rgba(165,184,106,.55),rgba(165,184,106,0) 70%);"></div>
    </div>
    <div class="panel flap-left"></div>
    <div class="panel back">
      <div class="art" role="img" aria-label="Vine flourish ornament" style="left:60px;top:8px;width:180px;height:34px;border-radius:17px;background:radial-gradient(rgba(95,114,54,.35),rgba(95,114,54,0) 70%);"></div>
      <div class="back-band">
        <div class="back-oval"><span class="brand"><span class="brand-mark" style="background:var(--olive);width:10px;height:10px"></span>Willow Naturals</span></div>
      </div>
    </div>
    <div class="panel flap-right"></div>
    <div class="panel front">
      <div class="brand"><span class="brand-mark" style="background:var(--leaf)"></span>Willow Naturals</div>
      <div class="script">Scented with Organic Essential Oils</div>
      <div class="art" role="img" aria-label="Green dahlia flower illustration" style="left:16px;top:82px;width:86px;height:86px;border-radius:50%;background:radial-gradient(#7b8f45,var(--olive) 60%,rgba(95,114,54,0) 72%);"></div>
      <div class="art" role="img" aria-label="Vine flourish ornament" style="left:150px;top:120px;width:110px;height:30px;border-radius:15px;background:radial-gradient(rgba(95,114,54,.35),rgba(95,114,54,0) 70%);"></div>
    </div>
    <div class="panel bottom">
      <div class="bottom-band">
        <div class="brand"><span class="brand-mark" style="background:var(--white)"></span>Willow Naturals</div>
        <div class="script">Suitable for Face, Hair, and Skin</div>
      </div>
      <div class="art" role="img" aria-label="Vine flourish ornament" style="left:150px;top:70px;width:120px;height:30px;border-radius:15px;background:radial-gradient(rgba(95,114,54,.3),rgba(95,114,54,0) 70%);"></div>
    </div>
  </section>

  <section class="label label-green">
    <div class="label-top"></div>
    <div class="label-frame">
      <div class="brand"><span class="brand-mark" style="background:var(--leaf)"></span>Willow Naturals</div>
      <div class="script">Suitable for Face, Hair, and Skin</div>
    </div>
    <div class="label-foot"><span class="script">Scented with Organic Essential Oils</span></div>
  </section>

  <section class="label label-plum">
    <div class="label-top"></div>
    <div class="label-frame">
      <div class="brand"><span class="brand-mark" style="background:var(--leaf)"></span>Willow Naturals</div>
      <div class="script">Suitable for Face, Hair, and Skin</div>
    </div>
    <div class="label-foot"><span class="script">Scented with Organic Essential Oils</span></div>
  </section>

  <section class="sleeve">
    <div class="sleeve-top script">Scented with Organic Essential Oils</div>
    <div class="art" role="img" aria-label="Pale green leaf ornament row" style="left:120px;top:34px;width:204px;height:36px;border-radius:18px;background:radial-gradient(rgba(165,184,106,.6),rgba(165,184,106,0) 70%);"></div>
    <div class="sleeve-band">
      <div class="brand"><span class="brand-mark"></span>Willow Naturals</div>
    </div>
    <div class="sleeve-foot script">Suitable for Face, Hair, and Skin</div>
  </section>

</main>
</body>
</html>
```